Tamarind Sailing needs a flyer promoting sailing holidays on the Coral Horizon Shoals

Tamarind Sailing is a private yacht charter company based in Sydney run by Mark & Jenny Dunford. We love sailing and our business allows us to share this passion with others. In winter 2015 (June - October) we're heading to Queensland, Australia to explore the Coral Horizon Shoals. We're offering sailing holidays on a large luxury yacht to small groups (max six guests on board, ideally four). We would like the design to complement our website (www.tamarindsailing.com.au) and reflect our tagline "where sailing meets fun and relaxation". I have attached a design brief with more information, some photos of previous trips to QLD and two versions of our logo.

Target Market(s)

Target markets are
-Small families (kid friendly) or couples with an interest in sailing or potential interest in sailing or
- Individuals who are learning to sail or love sailing or adventure travellers

Age bracket for both groups is 30-50.

Small families/couples will be professionals with well-paid jobs where they need a holiday where most things are done for them to wind down. They have a sense of adventure and would be bored just sitting on the beach. They like healthy living, fresh food and exercise, especially water sports (ideally sailing)

Individuals most likely will be learning to sail or adventure travellers looking for a different way to spend a few days away. They will earn a good wage in middle management, most likely come from the corporate world.

Industry/Entity Type

Business

Font styles to use
Sans Serif

Colors
0355a3
fece3f

Requirements
Must have
• Our Logo, contact details - name, email, website and phone no.
• Our Tagline.
Nice to have
• Wander Review logo, Chatterbook reference

```html
<!DOCTYPE html>
<html lang="en">
<head>
<meta charset="utf-8">
<title>Tamarind Sailing – Winter 2015 Flyer</title>
<link rel="stylesheet" href="https://fonts.googleapis.com/css2?family=Archivo+Black&family=Oswald:wght@400;500;600&family=Lato:wght@400;700&family=Roboto+Condensed:wght@700&display=swap">
<style>
  :root {
    --blue: #0355a3;
    --navy: #0c2c5c;
    --orange: #f7941d;
    --yellow: #fece3f;
    --red: #b3141b;
    --white: #ffffff;
    --sky: #7fb6e6;
    --sea: #1f8fc4;
    --sea-deep: #1a6f9a;
  }
  * { margin: 0; padding: 0; box-sizing: border-box; }
  html, body { width: 900px; height: 1200px; overflow: hidden; background: #ffffff; }
  .flyer { position: relative; width: 900px; height: 1200px; overflow: hidden; background: var(--white); font-family: "Lato", sans-serif; }

  .hero-photo {
    position: absolute; left: 0; top: 0; width: 900px; height: 600px;
    background: linear-gradient(180deg, var(--sky) 0%, #a9d3ee 10%, #6a9a5c 11%, #4f7d45 15%, #e8e3cf 17%, #3fb2d8 20%, var(--sea) 55%, var(--sea-deep) 100%);
  }
  .shapes { position: absolute; left: 0; top: 0; width: 900px; height: 1200px; }

  .photo-circle { position: absolute; border-radius: 50%; border: 6px solid var(--orange); background: var(--white); }
  .photo-circle .inner { width: 100%; height: 100%; border-radius: 50%; }
  .photo-beach { left: 46px; top: 279px; width: 200px; height: 200px; }
  .photo-beach .inner { background: linear-gradient(180deg, #9cc7ea 0%, #f5d9a8 50%, #6f8ea6 58%, #c9b07e 100%); }
  .photo-palm { left: 66px; top: 736px; width: 180px; height: 180px; border-color: #dfe3e8; border-width: 5px; }
  .photo-palm .inner { background: linear-gradient(180deg, #3f86d6 0%, #8fc0ec 45%, #3ca6c2 62%, #e9dcc0 80%, #d8c6a0 100%); }

  .brand { position: absolute; left: 56px; top: 552px; width: 300px; text-align: center; color: var(--navy); font-family: "Oswald", sans-serif; font-weight: 500; letter-spacing: 2px; }
  .brand .line { display: block; font-size: 32px; line-height: 38px; }

  .tagline { position: absolute; left: 40px; top: 638px; width: 560px; text-align: center; font-family: "Archivo Black", sans-serif; font-size: 36px; line-height: 44px; color: var(--blue); letter-spacing: 0.5px; }

  .season { position: absolute; left: 600px; top: 582px; width: 272px; height: 120px; background: var(--orange); color: var(--white); font-family: "Oswald", sans-serif; font-weight: 500; text-align: center; padding-top: 12px; }
  .season .year { display: block; font-size: 44px; line-height: 50px; }
  .season .months { display: block; font-size: 34px; line-height: 42px; }

  .intro { position: absolute; left: 604px; top: 710px; width: 268px; text-align: center; font-family: "Roboto Condensed", sans-serif; font-weight: 700; font-size: 19px; line-height: 25px; color: var(--blue); }
  .duration { position: absolute; left: 596px; top: 860px; width: 284px; text-align: center; font-family: "Oswald", sans-serif; font-weight: 500; font-size: 38px; line-height: 46px; color: var(--orange); }

  .offer { position: absolute; left: 292px; top: 752px; width: 300px; }
  .offer h2 { font-family: "Oswald", sans-serif; font-weight: 500; font-size: 44px; line-height: 50px; color: var(--orange); }
  .offer p { margin-top: 4px; font-family: "Lato", sans-serif; font-size: 23px; line-height: 30px; color: var(--navy); letter-spacing: 1px; text-transform: uppercase; }

  .guests { position: absolute; left: 55px; top: 916px; font-family: "Lato", sans-serif; font-size: 29px; line-height: 37px; color: var(--orange); letter-spacing: 1px; text-transform: uppercase; }

  .departures { position: absolute; left: 588px; top: 930px; width: 312px; height: 254px; background: var(--yellow); text-align: center; font-family: "Oswald", sans-serif; font-weight: 500; padding-top: 22px; }
  .departures .when { display: block; color: var(--orange); }
  .departures .where { display: block; color: var(--blue); }
  .departures .first-when { font-size: 56px; line-height: 64px; }
  .departures .first-where { font-size: 34px; line-height: 42px; }
  .departures .second-when { margin-top: 14px; font-size: 28px; line-height: 34px; }
  .departures .second-where { font-size: 23px; line-height: 30px; }

  .booking { position: absolute; left: 396px; top: 930px; width: 190px; height: 190px; }
  .booking-label { position: absolute; left: 401px; top: 977px; width: 180px; text-align: center; color: var(--white); font-family: "Oswald", sans-serif; font-weight: 500; font-size: 42px; line-height: 48px; }

  .contact { position: absolute; left: 44px; top: 1076px; color: var(--white); font-family: "Lato", sans-serif; font-size: 19px; line-height: 32px; letter-spacing: 0.5px; }
  .contact .row { display: flex; gap: 44px; font-size: 17px; }
</style>
</head>
<body>
<main class="flyer">
  <div class="hero-photo" role="img" aria-label="Photo of two snorkellers floating over a coral reef in clear turquoise water, with a sandy island and tree line behind"></div>

  <svg class="shapes" viewBox="0 0 900 1200" aria-hidden="true">
    <defs>
      <radialGradient id="seal-red" cx="50%" cy="40%" r="60%">
        <stop offset="0%" stop-color="#ee5a4f"/>
        <stop offset="100%" stop-color="#9e0f16"/>
      </radialGradient>
    </defs>
    <path d="M0,395 C160,440 320,480 480,482 C650,484 790,470 900,430 L900,600 L0,600 Z" fill="var(--orange)"/>
    <path d="M0,425 C170,490 330,528 500,526 C680,522 800,500 900,470 L900,600 L0,600 Z" fill="var(--blue)"/>
    <path d="M0,520 C220,500 480,570 700,560 C800,555 860,540 900,528 L900,600 L0,600 Z" fill="var(--orange)"/>
    <path d="M0,535 C220,515 470,590 700,582 C800,578 860,566 900,556 L900,1200 L0,1200 Z" fill="var(--white)"/>
    <path d="M0,1032 C150,995 330,990 600,1045 L600,1200 L0,1200 Z" fill="var(--orange)"/>
    <path d="M0,1060 C160,1032 360,1034 600,1092 C700,1112 820,1116 900,1106 L900,1200 L0,1200 Z" fill="var(--blue)"/>
    <path d="M0,1068 C160,1040 360,1042 600,1100" fill="none" stroke="var(--white)" stroke-width="3"/>
  </svg>

  <div class="photo-circle photo-beach"><div class="inner" role="img" aria-label="Photo of a sunset beach with yachts anchored offshore and a dinghy on the sand"></div></div>

  <div class="brand" aria-label="Tamarind Sailing">
    <span class="line">TAMARIND</span>
    <span class="line">SAILING</span>
  </div>

  <h1 class="tagline">WHERE SAILING MEETS<br>FUN AND RELAXATION</h1>

  <div class="season">
    <span class="year">WINTER 2015</span>
    <span class="months">(JUNE - OCTOBER)</span>
  </div>

  <p class="intro">Raise awareness of the opportunity to sail with us in the Whitsundays or other destinations on the Coral Horizon Shoals</p>
  <p class="duration">2 NIGHT 3 DAYS</p>

  <div class="photo-circle photo-palm"><div class="inner" role="img" aria-label="Photo of guests sitting on a leaning palm trunk over a tropical beach"></div></div>

  <section class="offer">
    <h2>WE OFFER</h2>
    <p>Sailing holidays<br>on a large luxury<br>yacht</p>
  </section>

  <p class="guests">Max six guests<br>on board</p>

  <div class="departures">
    <span class="when first-when">JUNE/JULY</span>
    <span class="where first-where">MAGNETIC ISLAND</span>
    <span class="when second-when">SEPTEMBER/OCTOBER</span>
    <span class="where second-where">MACKAY OR ROCKHAMPTON</span>
  </div>

  <svg class="booking" viewBox="-95 -95 190 190" aria-hidden="true">
    <polygon fill="var(--red)" points="92,0 75.3,20.2 79.7,46 55.2,55.2 46,79.7 20.2,75.3 0,92 -20.2,75.3 -46,79.7 -55.2,55.2 -79.7,46 -75.3,20.2 -92,0 -75.3,-20.2 -79.7,-46 -55.2,-55.2 -46,-79.7 -20.2,-75.3 0,-92 20.2,-75.3 46,-79.7 55.2,-55.2 79.7,-46 75.3,-20.2"/>
    <circle r="72" fill="url(#seal-red)"/>
  </svg>
  <p class="booking-label">BOOKING<br>ON</p>

  <footer class="contact">
    <div>CALL US : 0491 570 226</div>
    <div class="row"><span>www.tamarindsailing.com.au</span><span>info@tamarindsailing.com.au</span></div>
  </footer>
</main>
</body>
</html>
```